Walk Bright through the Seasons: 52 Weeks to a Year of Courage and Calm

This is a non-fiction, self-help book. The first edition was published a decade ago, and it needs a new design. Nothing too literal (no actual hearts on the cover) but something inspirational or perhaps something quite plain. The current cover is below for reference, but I DO NOT want something similar to that. It is outdated.

The cover must include:

1. Title: Walk Bright through the Seasons
2. Subtitle: 52 Weeks to a Year of Courage and Calm
3. Author Name: Tobin Wells

It should also have plenty of "white space" in other words the fonts shouldnt be so big that they take up the whole cover.

Dimensions: 9" x 6.25"

Target Market(s)

adults interested in personal development

Font styles to use
Serif
Script

Colors

Designer to choose colors to be used in the design.

Requirements
Must have
• Classic look and feel. The current design is too busy. I have included examples of the style I like below. I'm open to a singular graphic/photo but nothing more than that. Probably plain text is best.
• Please look at the samples I have included of best-selling books in the genre that I like. The cover should be modeled after these.

```html
<!DOCTYPE html>
<html lang="en">
<head>
<meta charset="utf-8">
<title>Walk Bright through the Seasons — Cover Wrap</title>
<link rel="stylesheet" href="https://fonts.googleapis.com/css2?family=Alegreya+Sans:wght@500;700;800;900&family=Dancing+Script:wght@500&display=swap">
<style>
  :root {
    --paper: #ffffff;
    --rule: #1a1a1a;
    --gold: #c4a066;
    --brown: #7a4a1e;
  }
  * { margin: 0; padding: 0; box-sizing: border-box; }
  html, body {
    width: 1200px;
    height: 823px;
    overflow: hidden;
    background: var(--paper);
  }
  .cover-wrap {
    position: relative;
    width: 1200px;
    height: 823px;
    border: 1.5px solid var(--rule);
    background: var(--paper);
    font-family: "Alegreya Sans", sans-serif;
  }
  .back-cover {
    position: absolute;
    left: 0; top: 0;
    width: 571px; height: 100%;
    border-right: 1.5px solid var(--rule);
  }
  .spine {
    position: absolute;
    left: 571px; top: 0;
    width: 58px; height: 100%;
    border-right: 1.5px solid var(--rule);
  }
  .spine-title {
    position: absolute;
    top: 84px;
    left: 50%;
    transform: translateX(-50%);
    writing-mode: vertical-rl;
    font-weight: 800;
    font-size: 30px;
    line-height: 1;
    color: var(--gold);
    white-space: nowrap;
  }
  .spine-author {
    position: absolute;
    top: 578px;
    left: 50%;
    transform: translateX(-50%);
    writing-mode: vertical-rl;
    font-weight: 700;
    font-size: 21px;
    letter-spacing: 0.32em;
    line-height: 1;
    color: var(--brown);
    white-space: nowrap;
  }
  .front-cover {
    position: absolute;
    left: 629px; top: 0;
    width: 571px; height: 100%;
  }
  .subtitle {
    position: absolute;
    top: 82px;
    left: 0; right: 0;
    text-align: center;
    font-weight: 800;
    font-size: 25px;
    letter-spacing: -0.01em;
    color: var(--brown);
  }
  .title {
    position: absolute;
    top: 262px;
    left: 180px;
    color: var(--gold);
    font-weight: 900;
    font-size: 84px;
    line-height: 88px;
    letter-spacing: -0.01em;
  }
  .title-line { display: block; white-space: nowrap; position: relative; }
  .title-script {
    font-family: "Dancing Script", cursive;
    font-weight: 500;
    font-size: 48px;
    color: var(--brown);
    letter-spacing: 0;
  }
  .title-script--after { margin-left: 6px; }
  .title-script--before {
    position: absolute;
    right: 100%;
    bottom: 14px;
    margin-right: 4px;
    line-height: 1;
  }
  .byline {
    position: absolute;
    top: 716px;
    left: 58px;
    right: 58px;
    display: flex;
    align-items: center;
    gap: 14px;
  }
  .byline-rule {
    flex: 1;
    height: 2px;
    background: var(--gold);
  }
  .byline-name {
    font-weight: 700;
    font-size: 20px;
    letter-spacing: 0.3em;
    margin-right: -0.3em;
    color: var(--brown);
    white-space: nowrap;
  }
</style>
</head>
<body>
  <main class="cover-wrap">
    <section class="back-cover" aria-label="Back cover"></section>

    <section class="spine" aria-label="Spine">
      <span class="spine-title">Walk Bright through the Seasons</span>
      <span class="spine-author">Tobin Wells</span>
    </section>

    <section class="front-cover" aria-label="Front cover">
      <p class="subtitle">” 52 Weeks to a Year of Courage and Calm ”</p>

      <h1 class="title">
        <span class="title-line">Walk</span>
        <span class="title-line">Bright<span class="title-script title-script--after">through</span></span>
        <span class="title-line"><span class="title-script title-script--before">the</span>Seasons</span>
      </h1>

      <div class="byline">
        <span class="byline-rule"></span>
        <span class="byline-name">Tobin Wells</span>
        <span class="byline-rule"></span>
      </div>
    </section>
  </main>
</body>
</html>
```